Rooted Ready Rising: Quiet Roots, Open Doors, Steady Hands

I want a modern and clean looking book cover. 5.25x8

Title
Rooted Ready Rising

Subtitle
Quiet Roots, Open Doors, Steady Hands

I don’t just want a graphic, I want it to make sense. If it can just be the words and a textured looking background, I’ll be ok with that too. I just want it to look crisp, clean, modern.

I want the back to have my book blurb and bio attached with the pic that’s attached.

Target Market(s)

Self help

Requirements
Must have
• Modern, clean look, look professional, attract customers.

```html
<!DOCTYPE html>
<html lang="en">
<head>
<meta charset="utf-8">
<title>Rooted Ready Rising — Book Cover Spread</title>
<link href="https://fonts.googleapis.com/css2?family=Anton&family=Open+Sans:wght@400;600;700;800&display=swap" rel="stylesheet">
<style>
  :root {
    --stage: #2f3034;
    --paper: #ffffff;
    --brand-red: #e3231c;
    --ink: #222222;
    --white: #ffffff;
    --photo-light: #f2f0ee;
    --photo-warm: #e6d3b8;
    --photo-amber: #c98f3e;
    --photo-dark: #3a2a20;
  }
  * { box-sizing: border-box; margin: 0; padding: 0; }
  html, body {
    width: 1200px; height: 1200px; overflow: hidden;
    background: var(--stage);
  }
  .spread { position: relative; width: 1200px; height: 1200px; }

  /* Back cover */
  .back-cover {
    position: absolute; left: 20px; top: 110px;
    width: 565px; height: 965px;
    background: var(--paper);
    font-family: "Open Sans", Arial, sans-serif;
    color: var(--ink);
  }
  .author-photo {
    position: absolute; left: 42px; top: 25px;
    width: 165px; height: 178px;
    background: linear-gradient(180deg, #e9e4e6 0%, #cfc4c8 55%, #3a3434 100%);
  }
  .bio-heading {
    position: absolute; left: 218px; top: 40px;
    font-size: 19px; font-weight: 700; color: var(--brand-red);
  }
  .bio-intro {
    position: absolute; left: 218px; top: 68px; width: 320px;
    font-size: 11.5px; line-height: 1.42;
  }
  .bio-intro strong { font-weight: 700; }
  .bio-more {
    position: absolute; left: 22px; top: 420px; width: 520px;
    font-size: 11.5px; line-height: 1.45;
  }
  .blurb-heading {
    position: absolute; left: 22px; top: 570px;
    font-size: 19px; font-weight: 700; color: var(--brand-red);
  }
  .blurb-box {
    position: absolute; left: 22px; top: 605px;
    width: 525px; height: 355px;
    background: var(--brand-red); color: var(--white);
    padding: 12px 12px;
    font-size: 11.4px; line-height: 1.42;
  }
  .blurb-box p + p { margin-top: 8px; }

  /* Front cover */
  .front-cover {
    position: absolute; left: 610px; top: 110px;
    width: 565px; height: 965px;
    overflow: hidden;
  }
  .cover-photo {
    position: absolute; inset: 0;
    background: linear-gradient(180deg,
      var(--photo-light) 0%,
      var(--photo-light) 42%,
      var(--photo-warm) 58%,
      var(--photo-amber) 76%,
      var(--photo-dark) 100%);
  }
  .cover-title {
    position: absolute; left: 52px; top: 78px;
    font-family: "Anton", Impact, sans-serif;
    color: var(--brand-red);
    font-size: 112px; line-height: 1.13;
    letter-spacing: 1px; text-transform: uppercase;
  }
  .cover-title span { display: block; }
  .cover-subtitle {
    position: absolute; left: 0; right: 0; bottom: 58px;
    text-align: center;
    font-family: "Open Sans", Arial, sans-serif;
    font-weight: 800; font-size: 19px;
    color: var(--white);
  }
</style>
</head>
<body>
<main class="spread">

  <section class="back-cover">
    <div class="author-photo" role="img" aria-label="Portrait photo of the author in a black t-shirt"></div>
    <h2 class="bio-heading">AUTHOR BIO:</h2>
    <p class="bio-intro"><strong>Renée Calloway</strong> is a helper. For as long as she can remember, she's always wanted to do the right thing, but life, circumstance, and some very tough years set her on a path that conflicted with what was in her heart... until something clicked and she made herself and her goals a priority. A dreamer and visionary at her core, she knew all too well how much faith and courage it takes to defy expectations and build your own path forward. Her tenacity led her in a direction that would change her life for the better.</p>
    <p class="bio-more">After being told she wasn't "college material" in high school, she made it her mission to never allow anyone to define who she is, and more importantly, to empower others to do the same. Today, the devout Christian, Author, Motivator, Coach, Educator, and Educational Leader holds 3 degrees (Bachelors of Science in Psychology, Master of Education, and Educational Specialist) and is currently in the dissertation phase of a Doctorate of Education. Recently, she added Life Coach to her resume. When she's not teaching, studying, coaching, reading, writing, listening to music, or helping others achieve their goals, she spends as much time as she can with her loving husband, three beautiful daughters, her college aged God-daughter, and countless friends.</p>
    <h2 class="blurb-heading">ROOTED, READY, RISING: Blurb:</h2>
    <div class="blurb-box">
      <p>Everyone has big dreams and lofty goals, but few give themselves permission to try.</p>
      <p>Rooted Ready Rising: Quiet Roots, Open Doors, Steady Hands is for anyone who has ever been stymied by negative self-talk, mistreatment, troubles at home, relationship problems, or has experienced anything significant that has made you want to abandon your dreams.</p>
      <p>Part memoir, part self help book, part spiritual guide, this book aims to provide encouragement and a helping hand to anyone who feels like life has passed them by or thinks their time will never come.</p>
      <p>Inside, you'll find deeply personal stories and anecdotes from Author Renée Calloway. Her personal experiences provide a detailed account and roadmap for how to lift yourself out of a dark spot, find your voice, dream bigger, dare to try, and change your life for the better.</p>
      <p>If you've ever felt like where you are now is where you'll always be, or fear that your prayers will never be answered, this book will help you move past obstacles, shatter expectations, and learn how to confidently bet on yourself because you're worth it. Scroll up and click "Buy Now" to find the support and motivation you need to move forward in life and finally be who you were meant to be!</p>
    </div>
  </section>

  <section class="front-cover">
    <div class="cover-photo" role="img" aria-label="Cover photograph area in light, warm amber and dark brown tones"></div>
    <h1 class="cover-title"><span>Rooted</span><span>Ready</span><span>Rising</span></h1>
    <p class="cover-subtitle">Quiet Roots, Open Doors, Steady Hands</p>
  </section>

</main>
</body>
</html>
```